LABEL FOR BOTTLE of Whiskey

We are launching a new Cinnamon and Walnut Whiskey called
Lanternfell

The Alc. by Vol. will be 45% and Proof 90. The size bottle will be 750ml

Target Market(s)

This will be for whiskey drinkers who enjoy experimenting with flavored whiskeys

Requirements
Must have
• Because the whiskey contains both walnuts and cinnamon both derived from trees, we chose the name lanternfell which describes the horticultural technique whereby tissues of plants are joined so as to continue their growth together as part of the tree.
Nice to have
• While subtle we would like for the design to have an element of nature, modern .. like a root, tree trunk with interwingled roots blending together, it can have a botanical illustration of botanical grafting (see examples)

or it could have a distinct beautiful combination of artsy leaves from the walnut tree leaves and leaves from the cinnamon tree together

```html
<!DOCTYPE html>
<html lang="en">
<head>
<meta charset="utf-8">
<title>Lanternfell Whiskey – Bottle Label</title>
<link rel="stylesheet" href="https://fonts.googleapis.com/css2?family=Rye&family=Oswald:wght@400;500&family=Ubuntu:wght@500;700&family=Pinyon+Script&display=swap">
<style>
  :root {
    --backdrop: #cccccc;
    --label-black: #231f20;
    --frame-line: #4a4240;
    --copper: #8b6242;
    --ink-white: #ffffff;
    --band-ink: #2b2220;
    --band-rule: #4a3526;
  }
  * { margin: 0; padding: 0; box-sizing: border-box; }
  html, body {
    width: 1200px; height: 850px; overflow: hidden;
    background: var(--backdrop);
  }
  .label {
    position: absolute; left: 309px; top: 30px;
    width: 582px; height: 790px;
    background: var(--label-black);
  }
  .label > * { position: absolute; }
  .label-frame {
    left: 28px; top: 31px; width: 526px; height: 732px;
    border: 1px solid var(--frame-line);
    outline: 1px solid var(--frame-line);
    outline-offset: -6px;
  }
  .ornament {
    background: radial-gradient(ellipse at center, rgba(139,98,66,.35), rgba(139,98,66,.08) 70%, transparent);
  }
  .ornament-crest { left: 190px; top: 52px; width: 220px; height: 62px; }
  .ornament-foot { left: 140px; top: 405px; width: 330px; height: 64px; }
  .ornament-side-left { left: 140px; top: 330px; width: 60px; height: 70px; }
  .ornament-side-right { left: 410px; top: 330px; width: 60px; height: 70px; }
  .flavour-arc { left: 0; top: 0; width: 582px; height: 160px; }
  .flavour-arc text {
    font-family: "Ubuntu", sans-serif; font-weight: 700;
    font-size: 15px; letter-spacing: 1px; fill: var(--ink-white);
  }
  .brand-name {
    left: 0; width: 582px; top: 182px; text-align: center;
    font-family: "Rye", serif; font-size: 58px; line-height: 1; font-weight: 400;
    color: var(--ink-white); white-space: nowrap;
  }
  .product-type {
    left: 0; width: 582px; top: 262px;
    display: flex; justify-content: center; align-items: center; gap: 12px;
    font-family: "Ubuntu", sans-serif; font-weight: 700;
    font-size: 20px; letter-spacing: 12px; color: var(--ink-white);
  }
  .product-type::before, .product-type::after {
    content: ""; width: 70px; height: 1px; background: var(--copper);
  }
  .estd, .estd-year {
    top: 348px; font-family: "Ubuntu", sans-serif; font-weight: 700;
    font-size: 15px; color: var(--ink-white); letter-spacing: 1px;
  }
  .estd { left: 210px; }
  .estd-year { left: 353px; }
  .spice-illustration {
    left: 266px; top: 322px; width: 80px; height: 50px; border-radius: 6px;
    background: linear-gradient(135deg, #6e4c33, #4a3424);
  }
  .recipe-note {
    left: 0; width: 582px; top: 380px; text-align: center;
    font-family: "Pinyon Script", cursive; font-size: 22px; color: #e6ddd4;
  }
  .spec-band { left: 0; top: 494px; width: 582px; height: 152px; }
  .spec-area { left: 0; top: 494px; width: 582px; height: 152px; }
  .spec-area > * { position: absolute; }
  .spec-line {
    display: flex; align-items: center; justify-content: center;
    font-family: "Oswald", "Arial Narrow", sans-serif; font-weight: 400;
    color: var(--band-ink); white-space: nowrap; line-height: 1;
  }
  .spec-big { font-size: 31px; height: 32px; letter-spacing: -0.5px; }
  .spec-small { font-size: 18px; height: 18px; }
  .col-strength { left: 89px; width: 110px; }
  .col-craft { left: 234px; width: 111px; }
  .spec-rule { height: 1px; background: var(--band-rule); }
  .spec-divider { width: 1px; top: 25px; height: 100px; background: var(--band-rule); }
  .grafting-illustration {
    left: 381px; top: 23px; width: 115px; height: 102px; border-radius: 4px;
    background: linear-gradient(180deg, rgba(43,34,32,.55), rgba(43,34,32,.3));
  }
  .story {
    left: 76px; width: 430px; top: 662px; text-align: center;
    font-family: "Ubuntu", sans-serif; font-weight: 500;
    font-size: 10.5px; line-height: 14px; color: var(--ink-white);
  }
  .website {
    left: 0; width: 582px; top: 712px; text-align: center;
    font-family: "Ubuntu", sans-serif; font-weight: 700;
    font-size: 20px; letter-spacing: 1px; color: var(--copper);
  }
</style>
</head>
<body>
  <main class="label">
    <div class="label-frame"></div>

    <div class="ornament ornament-crest" role="img" aria-label="Flourished scrollwork crest above the flavour line"></div>

    <svg class="flavour-arc" viewBox="0 0 582 160" aria-label="Cinnamon and Walnut">
      <defs><path id="flavour-curve" d="M200 142 Q 299 94 398 142"/></defs>
      <text><textPath href="#flavour-curve" startOffset="50%" text-anchor="middle">CINNAMON AND WALNUT</textPath></text>
    </svg>

    <h1 class="brand-name">LANTERNFELL</h1>
    <p class="product-type">WHISKEY</p>

    <div class="ornament ornament-side-left" role="img" aria-label="Scroll flourish"></div>
    <div class="ornament ornament-side-right" role="img" aria-label="Scroll flourish"></div>

    <span class="estd">ESTD.</span>
    <div class="spice-illustration" role="img" aria-label="Engraved illustration of walnuts and cinnamon sticks"></div>
    <span class="estd-year">2021</span>

    <p class="recipe-note">Original Recipe</p>

    <div class="ornament ornament-foot" role="img" aria-label="Flourished scrollwork beneath the emblem"></div>

    <svg class="spec-band" viewBox="0 0 582 152" preserveAspectRatio="none" aria-hidden="true">
      <defs>
        <pattern id="scallop-top" width="14" height="8" patternUnits="userSpaceOnUse">
          <circle cx="7" cy="8" r="7" fill="#8b6242"/>
        </pattern>
        <pattern id="scallop-bottom" width="14" height="8" patternUnits="userSpaceOnUse">
          <circle cx="7" cy="0" r="7" fill="#8b6242"/>
        </pattern>
      </defs>
      <rect x="0" y="0" width="582" height="6" fill="url(#scallop-top)"/>
      <rect x="0" y="6" width="582" height="140" fill="#8b6242"/>
      <rect x="0" y="146" width="582" height="6" fill="url(#scallop-bottom)"/>
    </svg>

    <section class="spec-area">
      <span class="spec-line spec-big col-strength" style="top:24px">45% VOL</span>
      <span class="spec-line spec-small col-strength" style="top:58px">ALCOHOL</span>
      <span class="spec-rule col-strength" style="top:86px"></span>
      <span class="spec-line spec-big col-strength" style="top:95px">PROF 90%</span>

      <span class="spec-divider" style="left:217px"></span>

      <span class="spec-line spec-big col-craft" style="top:22px">ARTFULLY</span>
      <span class="spec-line spec-big col-craft" style="top:54px">CRAFTED</span>
      <span class="spec-rule col-craft" style="top:91px"></span>
      <span class="spec-line spec-big col-craft" style="top:97px">750 ML</span>

      <span class="spec-divider" style="left:362px"></span>

      <div class="grafting-illustration" role="img" aria-label="Sketch of grafted branches joined into tree stumps"></div>
    </section>

    <p class="story">Grafting is a technique that joins two plants into one. In general, a wound is created on one of the plants, and the other is inserted into that wound so each plant’s tissues can grow together.</p>

    <p class="website">WWW.LANTERNFELLWHISKEY.COM</p>
  </main>
</body>
</html>
```